BUSINESS CARD MIRELLE CAVANOSI

I need a new business card for my personal business.
I am a Naturopath and Nutritionist working doing private consults in the health and wellness arena.
I would like to see designs that are, clean minimalist but colourful.
I like:
White (clean,fresh, minimalist)
pops of one colour ONLY.Choose a colour to run with and keep it simple.
green
light blue
mustard
Bright yellow
Charcoal
The final design should communicate professionalism but also be in touch with nature.
Key Information to include:
MIRELLE CAVANOSI
ABN 48 217 603 915
RQTLBE 327081
Tel 0487 639 142
NATUROPATH | HERBALIST | NUTRITON CONSULTANT
BHSc (Naturopathic Studies) Grad Dip (Naturopathy)
BACK OF CARD : YOUR NEXT APPOINTMENT ..................................
I already have a logo (picture attached)But I would be more than happy to NOT have this included. I am very Open to cards WITHOUT current logo/ ones that weave the colour of my logo but do not use the logo.
I have included pictures attached to give examples of the styles/colors I enjoy.
Updates
I have added a picture of a mortar and pestle - one just like this would be lovely to include in your entry.
TIA

```html
<!DOCTYPE html>
<html lang="en">
<head>
<meta charset="utf-8">
<title>Mirelle Cavanosi — Business Card</title>
<link rel="stylesheet" href="https://fonts.googleapis.com/css2?family=Share+Tech+Mono&family=Advent+Pro:wght@200&family=Roboto+Condensed:wght@700&family=Montserrat:wght@700&display=swap">
<style>
  :root {
    --backdrop: #e4e3e1;
    --card: #f7f7f5;
    --ink: #151515;
    --ink-soft: #8a8a8a;
    --accent: #1db39a;
    --emboss: #e2e2df;
  }
  * { margin: 0; padding: 0; box-sizing: border-box; }
  html, body {
    width: 1200px; height: 1200px; overflow: hidden;
    background: var(--backdrop);
  }
  .canvas { position: relative; width: 1200px; height: 1200px; }

  .card {
    position: absolute; left: 280px; width: 640px; height: 380px;
    background: var(--card);
    border-bottom: 6px solid var(--accent);
  }
  .card--back { top: 190px; }
  .card--front { top: 630px; }

  /* Back */
  .credentials {
    position: absolute; left: 56px; top: 60px;
    font-family: "Share Tech Mono", monospace;
    font-size: 17px; line-height: 21px; letter-spacing: 3px;
    color: var(--ink-soft);
  }
  .credentials .label { color: var(--ink); font-weight: 700; }
  .credentials .row--tel { text-decoration: underline; text-decoration-color: var(--ink); }
  .credentials .gap { height: 21px; }

  .appointment {
    position: absolute; right: 56px; top: 225px;
    font-family: "Montserrat", sans-serif; font-weight: 700;
    font-size: 15px; letter-spacing: 7px; color: var(--ink);
  }
  .dots {
    position: absolute; left: 56px; right: 56px; top: 270px; height: 80px;
  }

  /* Front */
  .emblem { position: absolute; left: 200px; top: 40px; }
  .identity {
    position: absolute; left: 0; right: 0; top: 150px; text-align: center;
  }
  .identity__name {
    font-family: "Advent Pro", sans-serif; font-weight: 200;
    font-size: 50px; letter-spacing: 8px; color: #6f6f6f;
    line-height: 1;
  }
  .identity__roles {
    margin-top: 12px;
    font-family: "Roboto Condensed", sans-serif; font-weight: 700;
    font-size: 15px; letter-spacing: 2.5px; color: var(--ink);
  }
</style>
</head>
<body>
<div class="canvas">

  <section class="card card--back" aria-label="Card back">
    <div class="credentials">
      <div><span class="label">ABN</span> 48 217 603 915</div>
      <div><span class="label">RQTLBE</span> 327081</div>
      <div class="row--tel"><span class="label">TEL</span> 0487 639 142</div>
      <div class="gap"></div>
      <div><span class="label">BHSC</span> (NATUROPATHIC STUDIES)</div>
      <div><span class="label">GRAD DIP</span> (NATUROPATHY)</div>
    </div>
    <div class="appointment">NEXT APPOINTMENT</div>
    <svg class="dots" viewBox="0 0 528 80" width="528" height="80" aria-hidden="true">
      <line x1="500" y1="6" x2="260" y2="6" stroke="#151515" stroke-width="4" stroke-linecap="round" stroke-dasharray="0 18"/>
      <line x1="8" y1="66" x2="440" y2="66" stroke="#151515" stroke-width="4" stroke-linecap="round" stroke-dasharray="0 18"/>
    </svg>
  </section>

  <section class="card card--front" aria-label="Card front">
    <svg class="emblem" width="240" height="300" viewBox="0 0 240 300" aria-hidden="true">
      <ellipse cx="120" cy="150" rx="118" ry="140" fill="none" stroke="var(--emboss)" stroke-width="3"/>
    </svg>
    <div class="identity">
      <div class="identity__name">MIRELLE CAVANOSI</div>
      <div class="identity__roles">NATUROPATH | HERBALIST | NUTRITON CONSULTANT</div>
    </div>
  </section>

</div>
</body>
</html>
```